Zo Fen smart screen Flyer design

Hi,

Please see attached file as I have done up a very very basic flyer just with the information that will need to be presented.

Please don't go with this as a format I would like, as I have no design skills at all.

I'm looking for something that is basic but professional looking capturing this information.
I would prefer if the symbols were changed so they were all consistent and the colour scheme worked together with the logo.

If you can use the picture of the screen provided as I will replace this once my product has its photoshoot.

Thanks!

```html
<!DOCTYPE html>
<html lang="en">
<head>
<meta charset="utf-8">
<title>Zo Fen Smart Screen – Flyer</title>
<link rel="stylesheet" href="https://fonts.googleapis.com/css2?family=Bebas+Neue&family=Catamaran:wght@400&family=Oswald:wght@400;500&family=Questrial&display=swap">
<style>
  :root {
    --yellow: #fcd800;
    --magenta: #c44a9c;
    --cyan: #4cc8ec;
    --ink: #1c1c1e;
    --grey-text: #2a2a2a;
    --paper: #ffffff;
    --backdrop: #cdcdcd;
    --tint-cyan: #e3f5fb;
    --tint-pink: #f6e2ef;
    --tint-cream: #fff8dc;
  }
  * { box-sizing: border-box; margin: 0; padding: 0; }
  html, body { width: 1200px; height: 1200px; overflow: hidden; background: var(--backdrop); }
  .flyer {
    position: absolute; left: 190px; top: 20px;
    width: 1170px; height: 1657px;
    transform: scale(0.7); transform-origin: top left;
    background: var(--paper); overflow: hidden;
    font-family: "Catamaran", sans-serif; color: var(--grey-text);
  }
  .abs { position: absolute; }
  .tint { position: absolute; }
  .tint--cyan { background: var(--tint-cyan); }
  .tint--pink { background: var(--tint-pink); }
  .tint--cream { background: var(--tint-cream); }

  .brand { left: 60px; top: 72px; display: flex; align-items: center; gap: 18px; }
  .brand__square { width: 34px; height: 34px; background: var(--magenta); }
  .brand__name { font-family: "Questrial", sans-serif; font-size: 66px; color: var(--ink); letter-spacing: 2px; line-height: 1; }
  .brand__tag { left: 62px; top: 158px; font-family: "Questrial", sans-serif; font-size: 22px; letter-spacing: 17px; color: var(--ink); }

  .frame { left: 0; top: 0; }
  .screen-photo { left: 0; top: 0; }

  .headline { font-family: "Bebas Neue", sans-serif; color: var(--ink); text-shadow: 4px 2px 0 #bdbdbd; line-height: 1; white-space: nowrap; }
  .headline--1 { left: 93px; top: 293px; font-size: 90px; letter-spacing: -1px; }
  .headline--2 { left: 93px; top: 388px; font-size: 66px; letter-spacing: -0.5px; }
  .headline--3 { left: 93px; top: 464px; font-size: 62px; letter-spacing: -0.5px; }
  .headline--hero { left: 88px; top: 527px; font-size: 165px; color: var(--yellow); text-shadow: none; letter-spacing: -1px; }

  .benefits { left: 60px; top: 908px; width: 450px; list-style: none; }
  .benefit { position: absolute; left: 0; display: flex; gap: 18px; font-size: 29px; line-height: 35.5px; letter-spacing: -0.2px; }
  .benefit__tick { flex: none; width: 40px; height: 40px; margin-top: 4px; }
  .benefit__text { width: 380px; text-align: justify; text-align-last: left; }

  .feature { position: absolute; left: 630px; width: 486px; }
  .feature__title { font-family: "Questrial", sans-serif; font-size: 30px; color: var(--ink); line-height: 1; margin-bottom: 8px; white-space: nowrap; }
  .feature__text { font-family: "Questrial", sans-serif; font-size: 20.5px; line-height: 26px; width: 380px; text-align: justify; text-align-last: left; }
  .feature__icon { position: absolute; left: 414px; width: 72px; height: 72px; border-radius: 12px; background: var(--ink); }

  .footer-band { left: 0; top: 0; }
  .call { left: 70px; top: 1542px; width: 90px; height: 100px; }
  .call__number { left: 165px; top: 1545px; font-family: "Bebas Neue", sans-serif; font-size: 76px; color: var(--ink); line-height: 1; letter-spacing: -0.5px; white-space: nowrap; transform: scaleX(0.84); transform-origin: left top; }
  .call__cta { left: 170px; top: 1606px; font-family: "Bebas Neue", sans-serif; font-size: 36px; color: var(--ink); line-height: 1; white-space: nowrap; transform: scaleX(0.9); transform-origin: left top; }
  .footer-divider { left: 481px; top: 1544px; width: 2px; height: 94px; background: var(--ink); }
  .contact { left: 502px; top: 1582px; font-family: "Oswald", sans-serif; font-weight: 400; font-size: 30px; color: var(--ink); line-height: 1; letter-spacing: -0.5px; white-space: nowrap; transform: scaleX(0.86); transform-origin: left top; }
  .contact__dot { display: inline-block; width: 8px; height: 8px; border-radius: 50%; background: var(--ink); margin: 0 14px 6px; vertical-align: middle; }
</style>
</head>
<body>
<main class="flyer">

  <svg class="abs" width="1170" height="140" viewBox="0 0 1170 140" aria-hidden="true" style="left:0;top:0">
    <polygon points="0,0 1170,0 1170,87 560,2 0,32" fill="var(--yellow)"/>
    <polygon points="560,2 1170,87 1170,102" fill="var(--cyan)"/>
    <polygon points="560,2 1170,102 1170,132" fill="var(--magenta)"/>
  </svg>

  <div class="tint tint--cyan" style="left:600px;top:60px;width:75px;height:55px"></div>
  <div class="tint tint--pink" style="left:755px;top:57px;width:157px;height:117px"></div>
  <div class="tint tint--pink" style="left:713px;top:145px;width:74px;height:55px"></div>
  <div class="tint tint--cream" style="left:590px;top:217px;width:93px;height:30px"></div>
  <div class="tint tint--cream" style="left:1083px;top:227px;width:82px;height:93px"></div>
  <div class="tint tint--cyan" style="left:88px;top:1377px;width:73px;height:53px"></div>
  <div class="tint tint--pink" style="left:242px;top:1377px;width:156px;height:113px"></div>
  <div class="tint tint--pink" style="left:200px;top:1460px;width:42px;height:30px"></div>

  <div class="brand abs">
    <span class="brand__square"></span>
    <span class="brand__name">Zo Fen</span>
  </div>
  <div class="brand__tag abs">SMART SCREEN</div>

  <svg class="frame abs" width="1170" height="820" viewBox="0 0 1170 820" aria-hidden="true">
    <polygon points="63,234 1113,267 1113,762 63,797" fill="none" stroke="var(--ink)" stroke-width="6"/>
  </svg>

  <svg class="screen-photo abs" width="1170" height="820" viewBox="0 0 1170 820" role="img" aria-label="Photo of an outdoor LED display cabinet showing children running across a green field">
    <defs>
      <linearGradient id="screenFace" x1="0" y1="0" x2="0" y2="1">
        <stop offset="0" stop-color="#5f8fc9"/>
        <stop offset="0.35" stop-color="#9cc0e0"/>
        <stop offset="0.55" stop-color="#7fb63c"/>
        <stop offset="1" stop-color="#4f9a2a"/>
      </linearGradient>
      <linearGradient id="screenReflect" x1="0" y1="0" x2="0" y2="1">
        <stop offset="0" stop-color="#8cc06a" stop-opacity="0.7"/>
        <stop offset="1" stop-color="#ffffff" stop-opacity="0"/>
      </linearGradient>
    </defs>
    <polygon points="1020,240 1085,256 1085,700 1020,697" fill="#15161a"/>
    <polygon points="677,312 1020,240 1020,697 677,690" fill="url(#screenFace)"/>
    <polygon points="677,690 1020,697 1085,700 1085,760 677,762" fill="url(#screenReflect)"/>
  </svg>

  <div class="headline headline--1 abs">BRING ATTNETION</div>
  <div class="headline headline--2 abs">TO YOUR BUSSINESS</div>
  <div class="headline headline--3 abs">WITH YOUR OWN</div>
  <div class="headline headline--hero abs">HD LED DISPLAY</div>

  <ul class="benefits abs">
    <li class="benefit" style="top:0">
      <svg class="benefit__tick" viewBox="0 0 40 40" aria-hidden="true"><path d="M33 12 A17 17 0 1 0 37 20" fill="none" stroke="var(--ink)" stroke-width="2.5" stroke-linecap="round"/><path d="M12 19 l7 8 l16 -18" fill="none" stroke="var(--ink)" stroke-width="2.5" stroke-linecap="round" stroke-linejoin="round"/></svg>
      <span class="benefit__text">Our displays can be mounted outdoors on walls, roofs, fixed signs, trailer mounted ect.</span>
    </li>
    <li class="benefit" style="top:183px">
      <svg class="benefit__tick" viewBox="0 0 40 40" aria-hidden="true"><path d="M33 12 A17 17 0 1 0 37 20" fill="none" stroke="var(--ink)" stroke-width="2.5" stroke-linecap="round"/><path d="M12 19 l7 8 l16 -18" fill="none" stroke="var(--ink)" stroke-width="2.5" stroke-linecap="round" stroke-linejoin="round"/></svg>
      <span class="benefit__text">We also do indoor led screens for shop fronts and display stands.</span>
    </li>
    <li class="benefit" style="top:363px">
      <svg class="benefit__tick" viewBox="0 0 40 40" aria-hidden="true"><path d="M33 12 A17 17 0 1 0 37 20" fill="none" stroke="var(--ink)" stroke-width="2.5" stroke-linecap="round"/><path d="M12 19 l7 8 l16 -18" fill="none" stroke="var(--ink)" stroke-width="2.5" stroke-linecap="round" stroke-linejoin="round"/></svg>
      <span class="benefit__text" style="text-align:left">All screens are cumtom built to your requirements including size, shape and even curved displays.</span>
    </li>
  </ul>

  <section class="feature" style="top:823px">
    <h3 class="feature__title">4G Capable</h3>
    <p class="feature__text">Change screen content with a click of the mouse anywhere in the world</p>
    <svg class="feature__icon" style="top:26px" viewBox="0 0 72 72" aria-hidden="true">
      <path d="M20 22 a22 22 0 0 1 32 0" fill="none" stroke="var(--yellow)" stroke-width="3.5" stroke-linecap="round"/>
      <path d="M25 28 a14 14 0 0 1 22 0" fill="none" stroke="var(--magenta)" stroke-width="3.5" stroke-linecap="round"/>
      <text x="36" y="58" text-anchor="middle" font-family="Oswald, sans-serif" font-weight="500" font-size="22" fill="#ffffff">4G</text>
    </svg>
  </section>

  <section class="feature" style="top:948px">
    <h3 class="feature__title">Wifi Capable</h3>
    <p class="feature__text">Change screen content with a PC, tablet or mobile phone with an easy to use app</p>
    <svg class="feature__icon" style="top:36px" viewBox="0 0 72 72" aria-hidden="true">
      <path d="M14 30 a32 32 0 0 1 44 0" fill="none" stroke="var(--yellow)" stroke-width="3.5" stroke-linecap="round"/>
      <path d="M20 37 a23 23 0 0 1 32 0" fill="none" stroke="var(--magenta)" stroke-width="3.5" stroke-linecap="round"/>
      <path d="M27 44 a13 13 0 0 1 18 0" fill="none" stroke="var(--cyan)" stroke-width="3.5" stroke-linecap="round"/>
      <circle cx="36" cy="52" r="3" fill="#ffffff"/>
    </svg>
  </section>

  <section class="feature" style="top:1090px">
    <h3 class="feature__title">Inteligent brightness control</h3>
    <p class="feature__text">Screen will automatically adjust to suit ambiant light improving screen veiwing quality and saving in power consumption</p>
    <svg class="feature__icon" style="top:42px" viewBox="0 0 72 72" aria-hidden="true">
      <circle cx="36" cy="32" r="9" fill="var(--yellow)"/>
      <g stroke="var(--magenta)" stroke-width="2.5" stroke-linecap="round">
        <line x1="36" y1="15" x2="36" y2="19"/><line x1="36" y1="45" x2="36" y2="49"/>
        <line x1="19" y1="32" x2="23" y2="32"/><line x1="49" y1="32" x2="53" y2="32"/>
        <line x1="24" y1="20" x2="27" y2="23"/><line x1="45" y1="41" x2="48" y2="44"/>
        <line x1="48" y1="20" x2="45" y2="23"/><line x1="27" y1="41" x2="24" y2="44"/>
      </g>
      <line x1="14" y1="57" x2="58" y2="57" stroke="var(--cyan)" stroke-width="2.5" stroke-dasharray="2 2"/>
    </svg>
  </section>

  <section class="feature" style="top:1262px">
    <h3 class="feature__title">Online Monitoring</h3>
    <p class="feature__text">Monitor cabinet temperature and humidity plus more in real time online. Recieve alerts via emial.</p>
    <svg class="feature__icon" style="top:32px" viewBox="0 0 72 72" aria-hidden="true">
      <rect x="23" y="14" width="9" height="30" rx="4.5" fill="none" stroke="var(--cyan)" stroke-width="3"/>
      <circle cx="27.5" cy="50" r="6" fill="var(--cyan)"/>
      <rect x="40" y="14" width="9" height="30" rx="4.5" fill="none" stroke="var(--yellow)" stroke-width="3"/>
      <circle cx="44.5" cy="50" r="6" fill="var(--yellow)"/>
      <line x1="44.5" y1="24" x2="44.5" y2="46" stroke="var(--magenta)" stroke-width="3"/>
    </svg>
  </section>

  <section class="feature" style="top:1412px">
    <h3 class="feature__title">High quality products</h3>
    <p class="feature__text">Setting high standard for colour, brightness and sharpness these LED modules will create attention.</p>
    <svg class="feature__icon" style="top:27px" viewBox="0 0 72 72" aria-hidden="true">
      <circle cx="36" cy="36" r="19" fill="var(--yellow)" stroke="var(--yellow)" stroke-width="5" stroke-dasharray="4 3"/>
      <circle cx="36" cy="36" r="9" fill="var(--magenta)"/>
      <path d="M31.5 36 l3 3 l6 -6" fill="none" stroke="#ffffff" stroke-width="2.2" stroke-linecap="round" stroke-linejoin="round"/>
    </svg>
  </section>

  <svg class="footer-band abs" width="1170" height="1657" viewBox="0 0 1170 1657" aria-hidden="true" style="pointer-events:none">
    <polygon points="0,1559 226,1484 1170,1597 1170,1657 0,1657" fill="var(--yellow)"/>
  </svg>

  <svg class="call abs" viewBox="0 0 90 100" aria-hidden="true">
    <path d="M20 6 h10 l4 22 l-9 6 c0 14 6 28 12 34 l9 -5 l13 18 l-8 9 c-24 4 -40 -24 -40 -52 c0 -16 3 -28 9 -32z" fill="var(--ink)"/>
    <path d="M58 38 a14 14 0 0 1 0 22" fill="none" stroke="var(--ink)" stroke-width="5" stroke-linecap="round"/>
    <path d="M66 30 a24 24 0 0 1 0 38" fill="none" stroke="var(--ink)" stroke-width="5" stroke-linecap="round"/>
    <path d="M74 22 a34 34 0 0 1 0 54" fill="none" stroke="var(--ink)" stroke-width="5" stroke-linecap="round"/>
  </svg>
  <div class="call__number abs">1300 ZOFENWA</div>
  <div class="call__cta abs">FOR A FREE QUOTE</div>
  <div class="footer-divider abs"></div>
  <div class="contact abs">info@zofenscreens.com.au<span class="contact__dot"></span>www.zofenscreens.com.au</div>

</main>
</body>
</html>
```